Website redesign

We've inherited a Tilecraft Website that we'd like to change to a Pagemill website to match our other sites.

Site I want redesigned is: https://www.corvellawings.com/
which will change to www.corvellaskytours.com.au

Our other websites I want it to match:
https://marloweskytours.com.au/
https://penfaricays.au/
https://tindaleskytours.com.au/
https://brightvalewings.com.au/

I do not want the design to deviate too much from the others, the main difference will be colours that need to align with the logo I've uploaded.

Pages I want:
Home
About Us
Gallery
News/Blog
Overflies
Half Day Tours
Full Day Tours
Transfers
Contact

Other pages will link to the other website - like on the other websites currently

```html
<!DOCTYPE html>
<html lang="en">
<head>
<meta charset="utf-8">
<title>Corvella Sky Tours – Scenic Flights</title>
<link rel="stylesheet" href="https://fonts.googleapis.com/css2?family=Lato:wght@400;600;700&display=swap">
<style>
:root{
  --ink:#111;
  --text:#333;
  --muted:#555;
  --green:#7cb342;
  --blue:#4a8fcf;
  --navy:#2e6aa6;
  --pale:#e7f1f4;
  --iconbg:#e3eef6;
  --line:#dcdcdc;
  --white:#fff;
  --black:#000;
}
*{box-sizing:border-box;margin:0;padding:0}
html,body{width:1200px;height:4389px;overflow:hidden}
body{font-family:'Lato',sans-serif;color:var(--text);background:var(--white);position:relative}
.abs{position:absolute}
.btn{position:absolute;display:flex;align-items:center;justify-content:center;font-size:15px;font-weight:600;color:var(--white);background:var(--green);border-radius:4px;text-transform:uppercase}
.ph{position:absolute;border-radius:10px}

.topbar{position:absolute;left:0;top:0;width:1200px;height:42px;background:var(--black);color:var(--white);font-size:13px}
.topbar span{position:absolute;top:13px;display:flex;align-items:center;gap:7px}
.dot{width:13px;height:13px;border-radius:50%;background:var(--white);display:inline-block}

.nav{position:absolute;top:42px;left:0;width:1200px;height:86px;background:var(--white);border-bottom:1px solid #eee}
.brand{position:absolute;left:90px;top:28px;display:flex;align-items:center;gap:10px;font-size:24px;font-weight:700;color:var(--navy)}
.brand i{width:28px;height:28px;border-radius:50%;background:var(--navy);display:block}
.menu{position:absolute;left:391px;top:35px;display:flex;gap:34px;font-size:13px;color:#444;text-transform:uppercase}
.menu .on{color:var(--blue)}
.book{left:899px;top:25px;width:140px;height:40px;background:var(--blue);font-size:15px}
.lang{position:absolute;left:1053px;top:35px;font-size:14px;color:#444}

.hero{position:absolute;top:128px;left:0;width:1200px;height:600px;background:linear-gradient(160deg,#3d6f78 0%,#4c8a8a 35%,#2f6570 60%,#1c3d47 100%)}
.hero h1{position:absolute;top:180px;width:100%;text-align:center;color:var(--white);font-size:47px;font-weight:700;line-height:56px;text-transform:uppercase}
.hero p{position:absolute;top:302px;width:100%;text-align:center;color:var(--white);font-size:24px;line-height:31px}

.about h2,.scenic h2{position:absolute;font-size:38px;font-weight:700;color:var(--ink);line-height:47px;text-transform:uppercase}
.body-text{position:absolute;font-size:15.5px;line-height:26px;color:var(--text)}
.stat{position:absolute;top:1283px;width:240px;text-align:center}
.stat .ic{width:86px;height:86px;border-radius:50%;background:var(--iconbg);margin:0 auto;display:flex;align-items:center;justify-content:center}
.stat b{display:block;font-size:41px;color:var(--green);margin-top:18px}
.stat em{display:block;font-style:normal;font-size:19px;color:var(--text);margin-top:10px}
.vr{position:absolute;top:1310px;width:1px;height:140px;background:var(--line)}

.scenic{position:absolute;top:1558px;left:0;width:1200px;height:504px;background:var(--pale)}

.sec-title{position:absolute;width:1200px;text-align:center;font-size:37px;font-weight:700;color:var(--ink);text-transform:uppercase}
.card{position:absolute;top:2215px;width:230px;height:281px;border-radius:8px}
.card-label{position:absolute;top:2516px;width:230px;text-align:center;font-size:23px;font-weight:700;color:var(--green);text-transform:uppercase}

.cta{position:absolute;top:2624px;left:0;width:1200px;height:446px;background:linear-gradient(180deg,#1f4f6b 0%,#2b7788 45%,#8a4a2f 70%,#2f7a88 100%)}
.cta h2{position:absolute;top:138px;width:100%;text-align:center;color:var(--white);font-size:38px;font-weight:700;line-height:47px;text-transform:uppercase}

.review{position:absolute;left:111px;top:3228px;width:978px;height:228px;border:2px solid #eee;border-radius:12px;box-shadow:0 2px 6px rgba(0,0,0,.06);text-align:center}
.review .badge{position:absolute;left:477px;top:36px;width:22px;height:22px;border-radius:50%;background:#d9d9d9}
.review p{margin:70px auto 0;width:680px;font-size:16px;line-height:26px;color:var(--text)}
.review strong{display:block;margin-top:12px;font-size:17px;font-weight:600;color:var(--green)}
.partner{position:absolute;top:3545px;width:120px;height:120px;background:#d9d9d9;border-radius:8px}

.tile{position:absolute;top:3770px;width:240px;height:162px}

.footer{position:absolute;top:3932px;left:0;width:1200px;height:457px;background:var(--black);color:var(--white)}
.footer h4{position:absolute;top:98px;font-size:21px;font-weight:600}
.footer .lnk{position:absolute;font-size:14.5px;line-height:39px}
.footer .contact{position:absolute;left:470px;font-size:14.5px;line-height:26px;display:flex;gap:18px}
.footer .about-text{position:absolute;left:111px;top:180px;width:290px;font-size:14.5px;line-height:26px}
.social{position:absolute;top:317px;display:flex;gap:14px;left:111px}
.social i{width:34px;height:34px;border-radius:50%;background:#3b5fb5;display:block}
.social i+i{background:#444}
.copy{position:absolute;top:416px;left:111px;width:978px;border-top:1px solid #333;padding-top:16px;text-align:center;font-size:13px}
</style>
</head>
<body>

<div class="topbar">
  <span style="left:111px"><svg width="13" height="13" viewBox="0 0 24 24"><path fill="#4a8fcf" d="M6.6 10.8a15 15 0 006.6 6.6l2.2-2.2a1 1 0 011-.25 11 11 0 003.6.6 1 1 0 011 1V20a1 1 0 01-1 1A17 17 0 013 4a1 1 0 011-1h3.5a1 1 0 011 1 11 11 0 00.6 3.6 1 1 0 01-.25 1z"/></svg>Call Us : 08 9100 4420</span>
  <span style="left:292px"><svg width="14" height="12" viewBox="0 0 24 20"><rect width="24" height="20" rx="2" fill="#4a8fcf"/><path d="M2 3l10 8 10-8" stroke="#fff" stroke-width="2" fill="none"/></svg>Email : info@brightvalewings.au</span>
  <span style="left:895px">Connect With Us : <i class="dot"></i><i class="dot"></i><i class="dot"></i></span>
</div>

<div class="nav">
  <div class="brand"><i></i>Corvella Sky Tours</div>
  <div class="menu">
    <span class="on">Home</span><span>About Us ⌄</span><span>Experiences ⌄</span><span>Transfers</span><span>Contact</span>
  </div>
  <div class="btn book">Bookings</div>
  <div class="lang">EN ⌄</div>
</div>

<div class="hero" role="img" aria-label="Aerial view over turquoise bay waters and islands from a small aircraft window">
  <h1>Explore Australia’s Last<br>Great Wilderness From The Sky</h1>
  <p>Fly over Corvella Bay's turquoise waters, red cliffs, and wild islands.<br>Experience the remote beauty of WA like never before.</p>
  <div class="btn" style="left:531px;top:395px;width:140px;height:41px">Learn More</div>
</div>

<section class="about">
  <div class="ph" style="left:111px;top:813px;width:325px;height:356px;background:linear-gradient(180deg,#a9c4de 0%,#d5d8dc 45%,#8d949a 100%)" role="img" aria-label="Small white aircraft parked on an airfield tarmac"></div>
  <div class="ph" style="left:338px;top:941px;width:219px;height:258px;border:3px solid #fff;background:linear-gradient(160deg,#c9b7a6 0%,#e6c7a8 40%,#6f8fa5 100%)" role="img" aria-label="Passenger taking photos through an aircraft window"></div>
  <h2 style="left:652px;top:810px">About Corvella<br>Sky Tours</h2>
  <p class="body-text" style="left:652px;top:930px;width:430px">Locally owned and operated, Corvella Sky Tours has been flying over Australia’s last great wilderness for over 30 years. Our experienced pilots offer breathtaking aerial tours over turquoise waters, red cliffs, and remote islands of this UNESCO World Heritage-listed region. We’re proud to provide a safe, unforgettable experience that reveals the true beauty of Corvella Bay — from above.</p>
  <div class="btn" style="left:652px;top:1147px;width:175px;height:41px">Discover More</div>

  <div class="stat" style="left:101px"><div class="ic"><svg width="46" height="46" viewBox="0 0 24 24"><path fill="#4a8fcf" d="M11 3h2v7l9 2v2l-9-1v5l3 2v1l-4-1-4 1v-1l3-2v-5l-9 1v-2l9-2z"/></svg></div><b>15+</b><em>Scenic Fights &amp; Charters</em></div>
  <div class="vr" style="left:389px"></div>
  <div class="stat" style="left:392px"><div class="ic"><svg width="40" height="46" viewBox="0 0 24 28"><path fill="#4a8fcf" d="M12 2a8 8 0 00-8 8c0 6 8 14 8 14s8-8 8-14a8 8 0 00-8-8zm0 11a3 3 0 110-6 3 3 0 010 6z"/><rect x="4" y="25" width="16" height="2" rx="1" fill="#4a8fcf"/></svg></div><b>5+</b><em>Destinations</em></div>
  <div class="vr" style="left:624px"></div>
  <div class="stat" style="left:627px"><div class="ic"><svg width="44" height="44" viewBox="0 0 24 24"><circle cx="17" cy="6" r="4" fill="#4a8fcf"/><circle cx="5" cy="19" r="2" fill="#4a8fcf"/><path d="M17 10v3H9a3 3 0 000 6h6" stroke="#4a8fcf" stroke-width="2" fill="none"/></svg></div><b>500+</b><em>Scenic Trips</em></div>
  <div class="vr" style="left:861px"></div>
  <div class="stat" style="left:871px"><div class="ic"><svg width="48" height="44" viewBox="0 0 28 24"><circle cx="14" cy="9" r="3.5" fill="#4a8fcf"/><circle cx="6" cy="11" r="2.5" fill="#4a8fcf"/><circle cx="22" cy="11" r="2.5" fill="#4a8fcf"/><path d="M8 22a6 6 0 0112 0zM1 22a5 5 0 019-2v2zM27 22a5 5 0 00-9-2v2z" fill="#4a8fcf"/><circle cx="14" cy="2" r="1.5" fill="#4a8fcf"/><circle cx="8" cy="4" r="1.2" fill="#4a8fcf"/><circle cx="20" cy="4" r="1.2" fill="#4a8fcf"/></svg></div><b>3500+</b><em>Happy Customers</em></div>
</section>

<section class="scenic">
  <h2 style="left:111px;top:70px">Scenic Flights And<br>Charter</h2>
  <p class="body-text" style="left:111px;top:189px;width:440px">Take to the skies with our unforgettable scenic flights over Corvella Bay’s most iconic landmarks — including Dirk Hartog Island, Francois Peron National Park, and Steep Point. Every passenger enjoys a guaranteed window seat, perfect for capturing stunning aerial views and unforgettable memories.</p>
  <div class="btn" style="left:112px;top:382px;width:140px;height:42px">Book Now</div>
  <div class="ph" style="left:609px;top:80px;width:479px;height:344px;background:linear-gradient(180deg,#e7a36f 0%,#c97f57 40%,#3a3638 75%,#2a2a2c 100%)" role="img" aria-label="Video of a small aircraft on a runway at sunset">
    <svg class="abs" style="left:16px;bottom:18px" width="448" height="14"><path d="M3 3l6 4-6 4z" fill="#fff"/><rect x="20" y="12" width="428" height="2" fill="rgba(255,255,255,.4)"/><rect x="20" y="12" width="250" height="2" fill="#fff"/></svg>
  </div>
</section>

<h2 class="sec-title" style="top:2140px">Explore Our Excursions</h2>
<div class="card" style="left:111px;background:linear-gradient(180deg,#6fa3d6 0%,#b8d8e8 35%,#4fb3c0 50%,#c98a5a 80%,#8a6a48 100%)" role="img" aria-label="Coastline with turquoise water and red sand"></div>
<div class="card" style="left:361px;background:linear-gradient(160deg,#c06a30 0%,#b6722f 35%,#2a9a9c 60%,#0f5e6a 100%)" role="img" aria-label="Aerial view of red cliffs meeting turquoise sea"></div>
<div class="card" style="left:609px;background:linear-gradient(180deg,#6b95c9 0%,#c9d6e0 25%,#7d6a4c 50%,#a3573a 100%)" role="img" aria-label="Red rock gorge landscape"></div>
<div class="card" style="left:858px;background:linear-gradient(180deg,#2b4f86 0%,#dfe7ee 25%,#3e7d96 45%,#d05a2b 70%,#b2482a 100%)" role="img" aria-label="Red coastal cliffs beside blue ocean"></div>
<div class="card-label" style="left:111px">Gascoyne</div>
<div class="card-label" style="left:361px">Pilbara</div>
<div class="card-label" style="left:609px">Murchison</div>
<div class="card-label" style="left:858px">Kimberley</div>

<section class="cta" role="img" aria-label="Aerial view of red sand dunes meeting turquoise ocean">
  <h2>Fly With Us And Discover Western<br>Australia's Beauty!</h2>
  <div class="btn" style="left:455px;top:257px;width:140px;height:41px">Book Now</div>
  <div class="btn" style="left:605px;top:257px;width:140px;height:41px;background:#111">Contact Us</div>
</section>

<h2 class="sec-title" style="top:3148px">What Customer Say About Us</h2>
<div class="review">
  <span class="badge"></span>
  <p>One of the best experiences of our trip to WA. The flight was smooth, the commentary was informative, and the scenery — just wow! Absolutely breathtaking! The views over Corvella Bay were unreal, and the pilot made us feel so safe and welcome.”</p>
  <strong>Priya L</strong>
</div>

<div class="partner" style="left:114px"></div>
<div class="partner" style="left:380px"></div>
<div class="partner" style="left:651px"></div>
<div class="partner" style="left:960px"></div>

<div class="tile" style="left:0;background:linear-gradient(180deg,#6fa0d8 0%,#c7ccd0 55%,#8a8f93 100%)" role="img" aria-label="Passengers beside an aircraft"></div>
<div class="tile" style="left:240px;background:linear-gradient(180deg,#2d63b8 0%,#8ab0d6 50%,#9b8672 100%)" role="img" aria-label="Group standing in front of a plane"></div>
<div class="tile" style="left:480px;background:linear-gradient(160deg,#9a6b4e 0%,#c0683a 45%,#4a9aa2 100%)" role="img" aria-label="Aerial view of red coastline"></div>
<div class="tile" style="left:720px;background:linear-gradient(180deg,#2f6fd1 0%,#6aa6e0 50%,#3b4a5a 100%)" role="img" aria-label="View from an aircraft cockpit"></div>
<div class="tile" style="left:960px;background:linear-gradient(160deg,#2a6a74 0%,#b85a34 50%,#3e8f96 100%)" role="img" aria-label="Aerial view of red cliffs and sea"></div>

<footer class="footer">
  <div class="brand" style="left:111px;top:95px;color:#4a8fcf;font-size:26px"><i style="background:#4a8fcf"></i>Corvella Sky Tours</div>
  <p class="about-text">Corvella Sky Tours is a locally owned operator offering unforgettable aerial tours over Western Australia's stunning Corvella Bay region.</p>
  <div class="social"><i></i><i></i><i></i></div>

  <h4 style="left:470px">Contact Us</h4>
  <div class="contact" style="top:145px"><svg width="18" height="20" viewBox="0 0 24 24"><path d="M12 2a7 7 0 00-7 7c0 5 7 13 7 13s7-8 7-13a7 7 0 00-7-7z" fill="none" stroke="#fff" stroke-width="1.6"/><circle cx="12" cy="9" r="2.5" fill="none" stroke="#fff" stroke-width="1.6"/></svg><span>14 Harlow Parade, Westmere,<br>WA, Australia, Western</span></div>
  <div class="contact" style="top:229px"><svg width="18" height="18" viewBox="0 0 24 24"><path d="M6.6 10.8a15 15 0 006.6 6.6l2.2-2.2a1 1 0 011-.25 11 11 0 003.6.6 1 1 0 011 1V20a1 1 0 01-1 1A17 17 0 013 4a1 1 0 011-1h3.5a1 1 0 011 1 11 11 0 00.6 3.6 1 1 0 01-.25 1z" fill="none" stroke="#fff" stroke-width="1.6"/></svg><span>08 9100 4420</span></div>
  <div class="contact" style="top:295px"><svg width="18" height="16" viewBox="0 0 24 20"><rect x="1" y="1" width="22" height="18" rx="2" fill="none" stroke="#fff" stroke-width="1.6"/><path d="M2 3l10 8 10-8" stroke="#fff" stroke-width="1.6" fill="none"/></svg><span>info@brightvalewings.au</span></div>

  <h4 style="left:777px">Main Links</h4>
  <div class="lnk" style="left:777px;top:133px">Home<br>About Us<br>Experiences<br>Transfers<br>Contact</div>

  <h4 style="left:941px">Other Links</h4>
  <div class="lnk" style="left:941px;top:133px">Support<br>Cookies Settings<br>Cookies Policy<br>Terms and Conditions<br>Privacy Policy</div>

  <div class="copy">Copyright © 2025 Corvella Sky Tours . All rights reserved.</div>
</footer>

</body>
</html>
```